Food Package Design (Soybean Rice Nuggets)

We Need package design for our new item. Here's detail:

BAG DIMENSION:
62/4 X 10 1/2 X 3 1/2 INCH
STAND UP BAG (ATTACHED PIC)
ARTWORK TEMPLATE ATTACHED (Please erase the contents in the attached template. Use the teamplte only).
At the end of the project, I will need printable, editable file with print die line

<Front side package>
The Crispy Crunchy Soybean Rice Nuggets
Belvri TM logo on top (*FILE UPLOADED)

Gluten Free
No Trans Fat
No Cholesterol
Net Weight 5 oz (142g)

<Back Side>
Soft and chewy rice puffs covered with roasted soybean powders. Belvri’s Soybean Rice Nuggets hit the other end of the spectrum. These are light, crunchy, crispy and savory and make a delicious that you might not be able to stop eating.

Ingredients: rice powder, palm oil, soybean powder, salt, sugar, corn grits

Contains soybean

Manufactured exclusively for Belvri (logo)
Tarrowfield, CA 90000
Made in Korea

www.belvrisnacks.example

Nutrition Facts (*File uploaded)
Serving Size 30g
Seriving Per Container About 5
Calories 140
Calories from Fat 45
Total Fat 5g 8%
Saturated Fat 2.5g 13%
Trans Fat 0g
Cholesterol 0mg 0%
Sodium 30mg 1%
Total Carbohydrate 22g 7%
Dietary Fiber 0g 0%
Sugars 4g
Protein 2g

Vitamin A 0%
Vitamin C 0%
Calcium 0%
Iron 0%

Barcode (*FILE UPLOADED)

* If I find a design I like, I could end my project earlier than deadline. I prefer to end the project sooner than deadline!
*If you need any images to purchase, please let me know.
Thank you for your participation and interest in our project!

Target Market(s)

HEALTH CONSCIOUS CONSUMERS, CONSUMER WHO LOVE SNACKING AND ALWAYS LOOKING FOR INNOVATIVE, UNIQUE, HEALTHY SNACKS.

Requirements
Must have
• FUN, BOLDNESS, MODERN, PLAYFUL, EYE CATCHING DESIGN

```html
<!DOCTYPE html>
<html lang="en">
<head>
<meta charset="utf-8">
<title>Belvri Soybean Rice Nuggets – Front Panel</title>
<link rel="stylesheet" href="https://fonts.googleapis.com/css2?family=Bebas+Neue&family=Fredoka:wght@600&family=Nunito:wght@600&display=swap">
<style>
  :root {
    --bg: #b5b5b5;
    --pouch: #232323;
    --orange: #e8911f;
    --orange-light: #f2a63a;
    --orange-deep: #d97d12;
    --white: #ffffff;
    --ink: #141414;
    --snack-light: #f2c98a;
    --snack-dark: #d08a3e;
    --leaf: #5f9a33;
    --bean: #e6cf8f;
  }
  * { margin: 0; padding: 0; box-sizing: border-box; }
  html, body { width: 1200px; height: 1200px; overflow: hidden; background: var(--bg); }
  .canvas { position: relative; width: 1200px; height: 1200px; }
  .pouch {
    position: absolute; left: 280px; top: 50px; width: 640px; height: 1100px;
    background: var(--pouch); border-radius: 26px 26px 10px 10px; overflow: hidden;
  }
  .pouch-art { position: absolute; inset: 0; }
  .brand {
    position: absolute; left: 38px; top: 140px;
    display: flex; align-items: center; gap: 10px;
    font-family: "Fredoka", sans-serif; font-weight: 600; font-size: 50px;
    color: var(--white);
  }
  .brand-dot { width: 20px; height: 20px; border-radius: 50%; background: var(--orange); }
  .title {
    position: absolute; left: 0; right: 0; top: 572px; text-align: center;
    font-family: "Bebas Neue", sans-serif; font-weight: 400; color: var(--white); line-height: 0.88;
  }
  .title-small { display: block; font-size: 74px; }
  .title-big { display: block; font-size: 98px; }
  .title-tail { display: block; font-size: 66px; }
  .weight {
    position: absolute; left: 241px; top: 940px; width: 156px; height: 156px;
    border-radius: 50%; background: var(--orange);
    display: flex; flex-direction: column; align-items: center; padding-top: 36px;
    font-family: "Nunito", sans-serif; font-weight: 600; font-size: 22px;
    color: var(--white); line-height: 1.2;
  }
  .claims {
    position: absolute; left: -10px; right: -10px; top: 880px; height: 62px;
    background: var(--orange); transform: rotate(-2deg);
    display: flex; align-items: center; justify-content: center; gap: 10px;
    font-family: "Fredoka", sans-serif; font-weight: 600; font-size: 25px; color: var(--ink);
  }
  .claim-light { color: var(--white); }
</style>
</head>
<body>
<div class="canvas">
  <div class="pouch">
    <svg class="pouch-art" width="640" height="1100" viewBox="0 0 640 1100">
      <defs>
        <linearGradient id="snackTone" x1="0" y1="0" x2="0" y2="1">
          <stop offset="0" stop-color="var(--snack-light)" stop-opacity="0.55"/>
          <stop offset="0.35" stop-color="var(--snack-light)"/>
          <stop offset="1" stop-color="var(--snack-dark)"/>
        </linearGradient>
        <linearGradient id="plantTone" x1="0" y1="0" x2="0" y2="1">
          <stop offset="0" stop-color="var(--leaf)"/>
          <stop offset="0.6" stop-color="#8fb44a"/>
          <stop offset="1" stop-color="var(--bean)"/>
        </linearGradient>
        <linearGradient id="bowlTone" x1="0" y1="0" x2="0" y2="1">
          <stop offset="0" stop-color="var(--orange-light)"/>
          <stop offset="1" stop-color="var(--orange-deep)"/>
        </linearGradient>
      </defs>
      <path role="img" aria-label="Soybean plant with leaves, green pods and a heap of dried soybeans"
            d="M470 90 Q580 40 640 70 L640 330 Q560 330 470 300 Q440 200 470 90 Z"
            fill="url(#plantTone)" opacity="0.9"/>
      <path d="M0 420 Q0 880 320 905 Q640 880 640 360 Z" fill="var(--orange-deep)"/>
      <ellipse role="img" aria-label="Crispy soybean rice nuggets tumbling down into a heaped bowl"
               cx="320" cy="340" rx="300" ry="250" fill="url(#snackTone)"/>
      <path d="M0 470 Q320 600 640 440 L640 520 Q630 880 320 905 Q10 880 0 520 Z"
            fill="url(#bowlTone)"/>
    </svg>

    <div class="brand"><span class="brand-dot"></span>Belvri</div>

    <h1 class="title">
      <span class="title-small">The Crispy</span>
      <span class="title-big">Crunchy</span>
      <span class="title-big">Soybean</span>
      <span class="title-tail">Rice Nuggets</span>
    </h1>

    <div class="weight"><span>Net Weight</span><span>5 oz (142g)</span></div>

    <div class="claims">
      <span>Gluten Free</span><span>|</span>
      <span class="claim-light">No Trans Fat</span><span>|</span>
      <span>No Cholesterol</span>
    </div>
  </div>
</div>
</body>
</html>
```